Exclusive beauty salon needs a price list or services booklet

I need a new very attractive flyer for my beauty salon, containing information on the different services and their prices.
In attachment you can find a pdf of the "old" one, but I'd love to have a beautifully designed new one!
I'd love to have a booklet in format 148 x 148 mm, or in US format, containing 12 or 16 pages, but if you can offer other nice looking designs they are welcome!
The services that need to come in the booklet with their prices can all be found on my website: www.atelierkova.be, starting with
Gelaatsverzorging
Wimperverlenging
Suikerontharing
Wimperlifting
Permanente Make Up
Airbrush Tanning

Target Market(s)

woman from 20 to 89 years old

Industry/Entity Type

Beauty Salon

Font styles to use
Sans Serif

Colors

Designer to choose colors to be used in the design.

Requirements
Must have
• a classy nice look, it must contain details about the services from my beauty salon and their prices, and nice pictures.
• The Names, prices and explanations of the services can easily be found on my website: www.atelierkova.be
Nice to have
• In attachment you can find the "old" price list in pdf, what I need now is a "new booklet" with the new logo and updated services price list.
• I need a very nice and attractive looking booklet, classy chique, Paris chique, looking very expensive.
Should not have
• Not too much colors, not too curly, but still feminine

```html
<!DOCTYPE html>
<html lang="nl">
<head>
<meta charset="utf-8">
<title>Salon brochure – Wimperverlenging &amp; Suikerontharing</title>
<link rel="stylesheet" href="https://fonts.googleapis.com/css2?family=Raleway:wght@400;500;700;800;900&display=swap">
<style>
  :root{
    --bg:#ece9e6;
    --paper:#ffffff;
    --paper-soft:#f7f7f8;
    --ink:#2b2b2b;
    --tab:#3a3334;
    --rose:#e7a9b4;
    --rose-light:#f9d7de;
    --rose-row:#f6c9d2;
    --photo-skin:#ead7cc;
    --photo-light:#f1efee;
  }
  *{margin:0;padding:0;box-sizing:border-box}
  html,body{width:1200px;height:1000px;overflow:hidden}
  body{background:var(--bg);font-family:"Raleway",sans-serif;color:var(--ink);position:relative}
  .spread{position:absolute;left:133px;width:935px;height:467px;display:flex;box-shadow:0 2px 8px rgba(0,0,0,.12)}
  .spread--lash{top:18px}
  .spread--sugar{top:505px}
  .page{position:relative;width:50%;height:100%;background:var(--paper);overflow:hidden}
  .page--right{background:var(--paper-soft)}
  .stripes{position:absolute;top:10px;height:20px;border-top:6px solid var(--rose-light);border-bottom:6px solid var(--rose-light)}
  .page--left .stripes{left:175px;right:0}
  .page--right .stripes{left:0;right:0}
  .title-tab{position:absolute;left:14px;top:0;width:161px;height:162px;background:var(--tab);border-radius:0 0 14px 14px;padding:0 10px 20px;display:flex;align-items:flex-end}
  .title-tab h1{color:var(--rose);font-weight:800;font-size:22px;line-height:1.28;letter-spacing:.3px}
  .page-no{position:absolute;right:2px;bottom:2px;width:26px;height:26px;background:var(--rose);color:#fff;font-size:9px;font-weight:700;display:flex;align-items:center;justify-content:center}
  .body-text{position:absolute;font-size:9.6px;line-height:1.25;color:#333}
  .body-text p{margin-bottom:11px}
  .body-text ul{list-style:none}
  .body-text li{position:relative;padding-left:10px}
  .body-text li::before{content:"";position:absolute;left:1px;top:3px;width:5px;height:5px;border-radius:50%;background:#222}
  .brand{position:absolute;font-weight:500;color:#555;letter-spacing:.4px}
  .photo{position:absolute}
  .price-note{position:absolute;left:111px;top:366px;font-weight:900;font-size:13px;line-height:1.25;color:#222}
  .intro{position:absolute;left:194px;top:118px;font-size:12.4px;line-height:1.3;text-transform:uppercase;font-weight:500;letter-spacing:.3px;color:#2b2b2b}
  .rates{position:absolute;left:11px;top:40px;width:196px;border-radius:12px;overflow:hidden;background:var(--paper)}
  .rates h2{background:var(--tab);color:var(--rose-light);font-size:12px;font-weight:800;text-align:center;padding:5px 0 6px;letter-spacing:.5px}
  .rates ul{list-style:none;background:var(--rose-row);padding:3px 0 6px}
  .rates li{display:flex;align-items:flex-end;font-size:9.2px;padding:3px 6px 2px;line-height:1.15;border-bottom:2px solid var(--paper)}
  .rates li:last-child{border-bottom:0}
  .rates .name{flex:0 1 auto}
  .rates .dots{flex:1;border-bottom:1px dotted #555;margin:0 2px 3px}
  .rates .price{flex:0 0 auto}
</style>
</head>
<body>

<section class="spread spread--lash">
  <div class="page page--left">
    <div class="stripes"></div>
    <div class="title-tab"><h1>WIMPERVER-<br>LENGING</h1></div>
    <div class="body-text" style="left:25px;top:190px;width:420px">
      <p>Lange, volle en gekrulde wimpers dankzij Silk Lash Studio. Zijden wimpers worden één per één op uw eigen wimpers gekleefd. Mascara kan maar is overbodig.</p>
      <p>Silk Lash Studio wimpers zijn ultralicht en zoveel natuurlijker dan kunststoffen wimperstrips, stukjes en plukjes. Door de exclusief ontwikkelde lijm blijven ze wekenlang in positie. De sneldrogende lijm laat een plaatsing toe van ongeveer 60 wimpers per oog. Een vol effect, in een behandeling van slechts 1/2 uur. Na max. 4 weken laten bijwerken garandeert een optimaal en schitterend eindresultaat.</p>
      <p>De zijden wimpers zijn beschikbaar in verchillende lengtes, diktes en krulling of curves.</p>
      <p style="margin-bottom:0">Voordelen van Silk Lash Studio Wimperverlenging op een rijtje</p>
      <ul>
        <li>Pijnloze behandeling</li>
        <li>Geen beschadiging van de natuurlijke wimpers</li>
        <li>Onmiddellijk een verbluffend resultaat</li>
        <li>Geen nazorg</li>
        <li>Verkrijgbaar in verschillende lengtes, diktes en curves</li>
        <li>Prima oplossing voor feestjes, vakanties, enz.</li>
        <li>Mascara wordt overbodig</li>
        <li>Wimperextensions blijven aangehecht tijdens het zwemmen, douchen en saunabezoek</li>
        <li>Silk Lash Studio garandeert wekenlang plezier</li>
      </ul>
    </div>
    <div class="page-no">03</div>
  </div>
  <div class="page page--right">
    <div class="stripes"></div>
    <div class="brand" style="right:30px;top:68px;font-size:21px">Silk Lash Studio</div>
    <div class="photo" role="img" aria-label="Close-up of lash extensions being applied with tweezers" style="left:31px;top:194px;width:196px;height:130px;background:linear-gradient(135deg,#d9bfb3,#f3ece8 55%,#c9a99b)"></div>
    <div class="photo" role="img" aria-label="Closed eyes before lash extensions" style="left:243px;top:194px;width:190px;height:63px;background:linear-gradient(180deg,#f0ddd3,#e6cbbf)"></div>
    <div class="photo" role="img" aria-label="Closed eyes after lash extensions" style="left:243px;top:260px;width:190px;height:66px;background:linear-gradient(180deg,#efdbd1,#e1c4b7)"></div>
    <p class="price-note">Eerste plaatsing wimperextensions €65<br>bijwerking na max. 4 weken €35</p>
    <div class="page-no">04</div>
  </div>
</section>

<section class="spread spread--sugar">
  <div class="page page--left">
    <div class="stripes"></div>
    <div class="title-tab"><h1>SUIKERON-<br>THARING</h1></div>
    <p class="intro">Heb je ook genoeg van lichaams-<br>en/of gezichtsbeharing maar ben<br>je niet tevreden met het resultaat<br>van scheren/harsen/laseren?<br>Dan is ontharen met suiker<br>van Velora dé oplossing!</p>
    <div class="body-text" style="left:20px;top:242px;width:425px">
      <p style="margin-bottom:2px">De voordelen van ontharen met suiker:</p>
      <ul>
        <li>De haren worden met de haargroeirichting verwijderd, hierdoor verminderd de pijn en je hebt geen last van haartjes die afbreken</li>
        <li>De haren worden volledig verwijderd (met de haarwortel) waardoor ze dunner en donziger worden en minder snel aangroeien</li>
        <li>Er wordt hygiënisch gewerkt</li>
        <li>De huidstructuur verbetert door het verwijderen van dode huidcellen zonder de levende cellen te beschadigen</li>
        <li>Suiker bestaat uit lichaamseigen stoffen waardoor de huid minder fel reageert op de ontharing.</li>
        <li>Suikerontharing zorgt ervoor dat de haargroei vermindert na iedere behandeling en verfijnt de haarstructuur</li>
        <li>met suikerontharing werkt men op lichaamstemperatuur dus geen brandwonden</li>
        <li>suikerontharing is geschikt voor de couperose huid en is uiterst geschikt voor de meest gevoelige plaatsen (bikini, gezicht,...)</li>
        <li>suiker is wateroplosbaar, dus geen ongewenste plakseltjes</li>
      </ul>
    </div>
    <div class="page-no">05</div>
  </div>
  <div class="page page--right">
    <div class="photo" role="img" aria-label="Woman in white seated on the floor showing smooth legs" style="left:0;top:0;width:100%;height:100%;background:radial-gradient(ellipse at 70% 70%,var(--photo-skin) 0,var(--photo-light) 45%,#f8f8f8 75%)"></div>
    <div class="stripes"></div>
    <div class="brand" style="left:290px;top:78px;font-size:25px;letter-spacing:1px">VELORA</div>
    <div class="rates">
      <h2>TARIEVEN</h2>
      <ul>
        <li><span class="name">Wenkbrauwen</span><span class="dots"></span><span class="price">€9</span></li>
        <li><span class="name">Wenkbrauwen en bovenlip</span><span class="dots"></span><span class="price">€16</span></li>
        <li><span class="name">Bovenlip of kin</span><span class="dots"></span><span class="price">€9</span></li>
        <li><span class="name">Bovenlip en kin</span><span class="dots"></span><span class="price">€16</span></li>
        <li><span class="name">Gezicht (bovenlip, kin,<br>wangen en wenkbrauw)</span><span class="dots"></span><span class="price">€25</span></li>
        <li><span class="name">Oksels</span><span class="dots"></span><span class="price">€12</span></li>
        <li><span class="name">Armen</span><span class="dots"></span><span class="price">€20</span></li>
        <li><span class="name">Brazilian bikini of string</span><span class="dots"></span><span class="price">€30</span></li>
        <li><span class="name">Bikinilijn</span><span class="dots"></span><span class="price">€15</span></li>
        <li><span class="name">Onderbeen en knie</span><span class="dots"></span><span class="price">€30</span></li>
        <li><span class="name">Bovenbenen</span><span class="dots"></span><span class="price">€20</span></li>
        <li><span class="name">Volledige benen (zonder<br>bikini)</span><span class="dots"></span><span class="price">€50</span></li>
        <li><span class="name">Volledige benen incl.<br>bikinilijn</span><span class="dots"></span><span class="price">€59</span></li>
      </ul>
    </div>
    <div class="page-no">06</div>
  </div>
</section>

</body>
</html>
```